Business Card Design

The new Company is called The Gilded Pecan - based in Miami Beach, Florida and Connecticut. We want a business card to be catchy and memorable ( like our Company name). Our business is marketing and retail sales of flavored cashew nuts in boutique /high end stores. The new business card must include a logo which must be a cashew nut with a king's crown or Roman wreath.
Yes- we are looking for a logo to be designed for the business and for the business card.

Industry/Entity Type

Marketing

Font styles to use
Script

```html
<!DOCTYPE html>
<html lang="en">
<head>
<meta charset="utf-8">
<title>The Gilded Pecan — Business Card</title>
<link rel="stylesheet" href="https://fonts.googleapis.com/css2?family=Open+Sans:wght@400;500&display=swap">
<style>
  :root {
    --page-bg: #f2f2f3;
    --card-black: #0c0c0c;
    --card-glow: #2a2a2a;
    --gold: #d4b06a;
    --gold-light: #f1d88f;
    --gold-dark: #a98544;
    --text-white: #ffffff;
    --divider: #bdbdbd;
  }
  * { margin: 0; padding: 0; box-sizing: border-box; }
  html, body {
    width: 1200px;
    height: 900px;
    overflow: hidden;
    background: var(--page-bg);
    font-family: "Open Sans", "Segoe UI", sans-serif;
  }
  .card {
    position: absolute;
    left: 64px;
    top: 119px;
    width: 1084px;
    height: 634px;
    background: radial-gradient(ellipse at 50% 40%, var(--card-glow) 0%, #151515 45%, var(--card-black) 100%);
    overflow: hidden;
  }
  .brand-mark {
    position: absolute;
    left: 488px;
    top: 66px;
    width: 120px;
    height: 120px;
    border-radius: 50%;
    background: radial-gradient(circle at 40% 35%, var(--gold-light), var(--gold) 55%, var(--gold-dark));
  }
  .brand-name {
    position: absolute;
    left: 0;
    right: 0;
    top: 255px;
    text-align: center;
    font-size: 60px;
    font-weight: 400;
    color: var(--gold);
    letter-spacing: 1px;
  }
  .gold-band {
    position: absolute;
    left: 0;
    top: 359px;
    width: 100%;
    height: 14px;
    background: linear-gradient(90deg, var(--gold-dark) 0%, var(--gold-light) 30%, var(--gold) 55%, var(--gold-light) 80%, var(--gold-dark) 100%);
  }
  .person {
    position: absolute;
    right: 593px;
    top: 430px;
    text-align: right;
  }
  .person-name {
    font-size: 38px;
    font-weight: 400;
    color: var(--gold);
    line-height: 1.1;
  }
  .person-title {
    font-size: 25px;
    color: var(--text-white);
    line-height: 1.3;
  }
  .divider {
    position: absolute;
    left: 541px;
    top: 411px;
    width: 2px;
    height: 153px;
    background: linear-gradient(180deg, transparent, var(--divider) 15%, var(--divider) 85%, transparent);
  }
  .contact-list {
    position: absolute;
    left: 572px;
    top: 416px;
    list-style: none;
  }
  .contact-item {
    display: flex;
    align-items: center;
    height: 35.5px;
    font-size: 27px;
    color: var(--text-white);
  }
  .contact-icon {
    width: 34px;
    height: 28px;
    margin-right: 16px;
    fill: var(--gold);
    flex-shrink: 0;
  }
</style>
</head>
<body>
  <main class="card">
    <div class="brand-mark"></div>
    <div class="brand-name">The Gilded Pecan</div>

    <div class="gold-band"></div>

    <div class="person">
      <div class="person-name">Marcus Hale</div>
      <div class="person-title">Managing Director</div>
    </div>

    <div class="divider"></div>

    <ul class="contact-list">
      <li class="contact-item">
        <svg class="contact-icon" viewBox="0 0 34 28" aria-hidden="true"><path d="M17 2 L2 15 h4 v11 h8 v-7 h6 v7 h8 V15 h4 Z"/></svg>
        PO Box 40518 FL 33139
      </li>
      <li class="contact-item">
        <svg class="contact-icon" viewBox="0 0 34 28" aria-hidden="true"><path d="M9 2 l5 6 -3 3 c2 4 5 7 9 9 l3 -3 6 5 -3 4 C15 26 6 17 6 5 Z"/></svg>
        1305 555 018
      </li>
      <li class="contact-item">
        <svg class="contact-icon" viewBox="0 0 34 28" aria-hidden="true"><path d="M3 9 h28 v17 H3 Z M3 9 l14 10 14 -10" stroke="#0c0c0c" stroke-width="1.5"/></svg>
        Marcus@gildedpecan.com
      </li>
      <li class="contact-item">
        <svg class="contact-icon" viewBox="0 0 34 28" aria-hidden="true"><circle cx="17" cy="14" r="12"/><path d="M5 14 h24 M17 2 v24 M7 8 h20 M7 20 h20 M17 2 c-6 6 -6 18 0 24 M17 2 c6 6 6 18 0 24" stroke="#0c0c0c" stroke-width="1.4" fill="none"/></svg>
        www.gildedpecan.com
      </li>
    </ul>
  </main>
</body>
</html>
```